Business card design and logo for plumbing bussiness

We are wanting a logo for a plumbing business is Queensland Australia. KRV Plumbing and Drainage will be doing works on domestic and commercial sites.
Plumbing, drainage and gas works. We are wanting something that will stand out and be noticed. Colours could be black blue and white but open for suggestions.

Target Market(s)

Builders and home renovators

Industry/Entity Type

Plumbing

Contact Information for Business Card

Miles Dorgan - Director
0417 582 913
miles@krvplumbing.example.com.au
QBCC: 847 2106
ABN: 52 319 407 281

Font styles to use
Sans Serif

Colors
000000

Requirements
Must have
• Clear defined branding

```html
<!DOCTYPE html>
<html lang="en">
<head>
<meta charset="utf-8">
<title>KRV Plumbing and Drainage – Business Card</title>
<link href="https://fonts.googleapis.com/css2?family=Roboto:wght@400;500&display=swap" rel="stylesheet">
<style>
  :root {
    --backdrop: #dcdcdc;
    --card: #ffffff;
    --brand-blue: #0094c9;
    --charcoal: #2d2d2d;
    --navy: #1f1a4a;
    --text: #2a2a2a;
  }
  * { margin: 0; padding: 0; box-sizing: border-box; }
  html, body {
    width: 1200px; height: 745px; overflow: hidden;
    background: var(--backdrop);
    font-family: "Roboto", Arial, sans-serif;
  }
  .stage { position: relative; width: 1200px; height: 745px; }
  .card {
    position: absolute; left: 370px; width: 462px; height: 256px;
    background: var(--card); overflow: hidden;
  }
  .card--front { top: 93px; }
  .card--back { top: 395px; }

  /* Front */
  .brand {
    position: absolute; left: 0; right: 0; top: 62px;
    display: flex; align-items: center; justify-content: center; gap: 14px;
  }
  .brand__dot { width: 46px; height: 46px; border-radius: 50%; background: var(--brand-blue); flex: none; }
  .brand__name {
    color: var(--brand-blue); font-weight: 500; font-size: 24px; line-height: 1.1;
    text-transform: uppercase; letter-spacing: 0.5px;
  }
  .band { position: absolute; left: 0; right: 0; }
  .band--blue { top: 216px; height: 16px; background: var(--brand-blue); }
  .band--dark { top: 232px; height: 24px; background: var(--charcoal); }

  /* Back */
  .block { position: absolute; }
  .block--dark-top { left: 0; top: 0; width: 30px; height: 40px; background: var(--charcoal); }
  .block--blue-top { left: 30px; top: 0; width: 44px; height: 40px; background: var(--brand-blue); }
  .block--dark-side { left: 0; top: 94px; width: 30px; height: 162px; background: var(--charcoal); }
  .block--blue-side { left: 30px; top: 94px; width: 44px; height: 162px; background: var(--brand-blue); }
  .block--blue-right { left: 433px; top: 40px; width: 29px; height: 53px; background: var(--brand-blue); }

  .person { position: absolute; left: 41px; top: 50px; }
  .person__name { color: var(--navy); font-weight: 500; font-size: 18px; line-height: 21px; }
  .person__role { color: var(--text); font-size: 11px; line-height: 13px; }

  .contact-icon {
    position: absolute; left: 39px; width: 26px; height: 26px;
    border-radius: 50%; background: var(--charcoal);
    display: flex; align-items: center; justify-content: center;
  }
  .contact-icon svg { width: 14px; height: 14px; }
  .contact-icon--phone { top: 118px; }
  .contact-icon--web { top: 155px; }
  .contact-icon--info { top: 190px; }

  .contact-line {
    position: absolute; left: 85px; color: var(--text);
    font-size: 11px; line-height: 13.5px;
  }
  .contact-line--phone { top: 124px; }
  .contact-line--email { top: 161px; }
  .contact-line--reg { top: 191px; }
</style>
</head>
<body>
<main class="stage">
  <section class="card card--front" aria-label="Business card front">
    <div class="brand">
      <span class="brand__dot"></span>
      <span class="brand__name">KRV Plumbing<br>and Drainage</span>
    </div>
    <div class="band band--blue"></div>
    <div class="band band--dark"></div>
  </section>

  <section class="card card--back" aria-label="Business card back">
    <div class="block block--dark-top"></div>
    <div class="block block--blue-top"></div>
    <div class="block block--dark-side"></div>
    <div class="block block--blue-side"></div>
    <div class="block block--blue-right"></div>

    <div class="person">
      <p class="person__name">Miles Dorgan</p>
      <p class="person__role">Director</p>
    </div>

    <span class="contact-icon contact-icon--phone">
      <svg viewBox="0 0 24 24" aria-hidden="true"><path fill="#fff" d="M6.6 10.8a15.1 15.1 0 0 0 6.6 6.6l2.2-2.2c.3-.3.7-.4 1-.2 1.1.4 2.3.6 3.6.6.6 0 1 .4 1 1V20c0 .6-.4 1-1 1A17 17 0 0 1 3 4c0-.6.4-1 1-1h3.5c.6 0 1 .4 1 1 0 1.3.2 2.5.6 3.6.1.3 0 .7-.2 1z"/></svg>
    </span>
    <span class="contact-icon contact-icon--web">
      <svg viewBox="0 0 24 24" aria-hidden="true" fill="none" stroke="#fff" stroke-width="1.8"><circle cx="12" cy="12" r="9"/><ellipse cx="12" cy="12" rx="4" ry="9"/><path d="M3 12h18M4.5 7.5h15M4.5 16.5h15"/></svg>
    </span>
    <span class="contact-icon contact-icon--info">
      <svg viewBox="0 0 24 24" aria-hidden="true"><circle cx="13.5" cy="4.5" r="2.3" fill="#fff"/><path fill="#fff" d="M9 9.5h5.5l-2.3 9h2.3l-.5 2H8.5l2.3-9H8.5z"/></svg>
    </span>

    <p class="contact-line contact-line--phone">0417 582 913</p>
    <p class="contact-line contact-line--email">miles@krvplumbing.example.com.au</p>
    <p class="contact-line contact-line--reg">QBCC: 847 2106<br>ABN: 52 319 407 281</p>
  </section>
</main>
</body>
</html>
```